Energy trading company (Voltrisa) needs a business card

We need a business card for a company based in Central America. Our main purpose is trading energy . We already have the logo but we need some good creativity to design a high impact business card. Colors blue, orange, green can be used or we would like to see good combinatios with our logo

Target Market(s)

Energy

Industry/Entity Type

Power Generation

Contact Information for Business Card

Logo , headquarters , name, background

Font styles to use
Serif
Sans Serif

Colors

Designer to choose colors to be used in the design.

Requirements
Must have
• it must have a fresh and clean view
Nice to have
• good backgrounds that combine with the logo
Should not have
• too much words

```html
<!DOCTYPE html>
<html lang="en">
<head>
<meta charset="utf-8">
<title>Voltrisa Business Card</title>
<link href="https://fonts.googleapis.com/css2?family=Lato:wght@400;700&display=swap" rel="stylesheet">
<style>
  :root {
    --backdrop: #6e5136;
    --card: #070808;
    --orange: #f47d20;
    --text-grey: #9c9c9c;
    --divider: #4a3320;
  }
  * { margin: 0; padding: 0; box-sizing: border-box; }
  html, body { width: 1200px; height: 1023px; overflow: hidden; }
  body {
    background: var(--backdrop);
    font-family: "Lato", sans-serif;
    position: relative;
  }
  .card {
    position: absolute;
    left: 248px;
    width: 681px;
    height: 390px;
    background: var(--card);
    box-shadow: -8px 8px 0 rgba(0,0,0,0.55);
  }
  .card-front { top: 87px; }
  .card-back { top: 541px; }

  .brand-mark {
    position: absolute;
    border-radius: 50%;
    background: var(--orange);
  }
  .brand-name {
    position: absolute;
    color: var(--orange);
    font-weight: 400;
    white-space: nowrap;
    line-height: 1;
  }

  .card-front .brand-mark { left: 153px; width: 66px; height: 66px; top: 139px; }
  .card-front .brand-name { left: 63px; width: 245px; text-align: center; top: 208px; font-size: 52px; }

  .divider {
    position: absolute;
    left: 340px;
    top: 104px;
    width: 1px;
    height: 182px;
    background: var(--divider);
  }

  .contact-block { position: absolute; left: 372px; top: 98px; color: var(--text-grey); }
  .person-name {
    color: var(--orange);
    font-weight: 700;
    font-size: 30px;
    line-height: 1;
    letter-spacing: 0.3px;
  }
  .person-role { font-size: 18px; margin-top: 9px; line-height: 1; }
  .address { font-size: 18px; line-height: 19px; margin-top: 15px; }
  .contact-list { list-style: none; margin-top: 12px; }
  .contact-list li {
    display: flex;
    align-items: center;
    height: 26px;
    font-size: 18px;
  }
  .contact-list svg { width: 17px; height: 17px; margin-right: 15px; flex: none; }

  .card-back .brand-mark { left: 297px; width: 86px; height: 86px; top: 114px; }
  .card-back .brand-name { left: 190px; width: 300px; text-align: center; top: 210px; font-size: 63px; }
</style>
</head>
<body>
  <section class="card card-front">
    <div class="brand-mark"></div>
    <div class="brand-name">VOLTRISA</div>
    <div class="divider"></div>
    <div class="contact-block">
      <div class="person-name">JOHN SMITH</div>
      <div class="person-role">Position</div>
      <div class="address">2345 First Address Line<br>Second Address Line, 56324</div>
      <ul class="contact-list">
        <li>
          <svg viewBox="0 0 24 24" aria-hidden="true"><path fill="var(--orange)" d="M6.6 10.8a15.1 15.1 0 0 0 6.6 6.6l2.2-2.2a1 1 0 0 1 1-.25 11.4 11.4 0 0 0 3.6.57 1 1 0 0 1 1 1V20a1 1 0 0 1-1 1A17 17 0 0 1 3 4a1 1 0 0 1 1-1h3.5a1 1 0 0 1 1 1c0 1.25.2 2.45.57 3.57a1 1 0 0 1-.25 1z"/></svg>
          123 456 7890
        </li>
        <li>
          <svg viewBox="0 0 24 24" aria-hidden="true"><rect x="2" y="5" width="20" height="14" fill="var(--orange)"/><path d="M2 5l10 8 10-8M2 19l7-7M22 19l-7-7" stroke="var(--card)" stroke-width="1.5" fill="none"/></svg>
          lorem@yourwebsite.com
        </li>
        <li>
          <svg viewBox="0 0 24 24" aria-hidden="true"><circle cx="12" cy="12" r="10" fill="var(--orange)"/><g stroke="var(--card)" stroke-width="1.2" fill="none"><ellipse cx="12" cy="12" rx="4" ry="10"/><path d="M2 12h20M4 7h16M4 17h16M12 2v20"/></g></svg>
          www.yourwebsite.com
        </li>
      </ul>
    </div>
  </section>

  <section class="card card-back">
    <div class="brand-mark"></div>
    <div class="brand-name">VOLTRISA</div>
  </section>
</body>
</html>
```